Attractive Wall Posters wanted

We are designing posters for our outdoor wall to represent our brands.

(Portrait Layout: Measurements - Height 128cm, Width 108cm).

More information for each brand can be found on the website listed in the ppt attached.

Requirements
Must have
• The information included in PPT, the logo, the website and the short description
Nice to have
• Consistency across all posters
Should not have
• too cluttered designs

```html
<!DOCTYPE html>
<html lang="en">
<head>
<meta charset="utf-8">
<title>Brightpath Learning – Corporate Training + Business Consultancy</title>
<link href="https://fonts.googleapis.com/css2?family=Libre+Caslon+Text:ital,wght@0,400;0,700;1,700&display=swap" rel="stylesheet">
<style>
  :root {
    --gold: #d6a52c;
    --white: #ffffff;
    --ink: #111111;
    --slate: #5f6166;
    --espresso: #2b1d1b;
    --photo-light: #e2ddd6;
    --photo-mid: #cbbfb3;
    --photo-warm: #9c7a66;
  }
  * { margin: 0; padding: 0; box-sizing: border-box; }
  html, body { width: 1013px; height: 1200px; overflow: hidden; background: var(--white); }
  body { font-family: "Libre Caslon Text", Georgia, serif; }
  .poster { position: relative; width: 1013px; height: 1200px; overflow: hidden; background: var(--white); }

  .hero-photo {
    position: absolute; left: 0; top: 269px; width: 1013px; height: 661px;
    background:
      radial-gradient(ellipse 260px 380px at 790px 420px, rgba(150,120,100,0.55), rgba(150,120,100,0) 70%),
      linear-gradient(180deg, var(--photo-light) 0%, var(--photo-mid) 70%, var(--photo-warm) 100%);
  }

  .brand-panel { position: absolute; left: 387px; top: 0; width: 626px; height: 306px; background: var(--gold); }
  .brand-notch { position: absolute; left: 0; top: 0; }
  .brand-tile { position: absolute; left: 0; top: 0; width: 387px; height: 269px; background: var(--white); }

  .brand-mark {
    position: absolute; left: 62px; top: 58px; width: 290px;
    font-weight: 400; font-size: 138px; line-height: 1; color: var(--gold);
    letter-spacing: -4px;
  }
  .brand-title {
    position: absolute; left: 30px; top: 70px; width: 596px;
    text-align: center; color: var(--white);
    font-weight: 400; font-size: 46px; line-height: 68px;
    white-space: nowrap;
  }

  .headline {
    position: absolute; left: 66px; top: 352px;
    font-weight: 700; font-size: 60px; line-height: 80px; letter-spacing: -1px;
    white-space: nowrap;
  }
  .headline .muted { color: var(--slate); display: block; }
  .headline .strong { color: var(--ink); display: block; }
  .headline .plus { display: inline-block; width: 36px; height: 36px; margin-left: 16px; vertical-align: 4px; }
  .tagline {
    position: absolute; left: 68px; top: 670px;
    font-style: italic; font-weight: 700; font-size: 32px; color: var(--ink);
    white-space: nowrap;
  }

  .description-band {
    position: absolute; left: 0; top: 930px; width: 1013px; height: 270px;
    background: var(--espresso);
  }
  .description {
    position: absolute; left: 67px; top: 56px;
    color: var(--gold); font-weight: 400; font-size: 35.5px; line-height: 51px;
    white-space: nowrap;
  }
</style>
</head>
<body>
<main class="poster">
  <div class="hero-photo" role="img" aria-label="Photo of a speaker holding a microphone in front of a blurred conference audience"></div>

  <header>
    <div class="brand-panel">
      <p class="brand-title">Brightpath Learning<br>www.BPLasia.com</p>
    </div>
    <div class="brand-tile"></div>
    <svg class="brand-notch" width="420" height="270" viewBox="0 0 420 270" aria-hidden="true">
      <polygon points="386,108 418,140 386,172" fill="#ffffff"/>
    </svg>
    <div class="brand-mark">BPL</div>
  </header>

  <h1 class="headline">
    <span class="muted">CORPORATE</span>
    <span class="strong">TRAINING<svg class="plus" viewBox="0 0 36 36" aria-label="plus"><path d="M12 0h12v12h12v12H24v12H12V24H0V12h12z" fill="#d6a52c"/></svg></span>
    <span class="muted">BUSINESS</span>
    <span class="strong">CONSULTANCY</span>
  </h1>
  <p class="tagline">&lt;The growth from within&gt;</p>

  <section class="description-band">
    <p class="description">Everything a successful organization needs<br>to train high performance teams to drive<br>corporate strategy and create societal impact</p>
  </section>
</main>
</body>
</html>
```